Business card design needed

www.corvanfab.com.au
Our primary services:
On-site welding.
On-site industrial maintenance.
On-site repairs and capital works projects specialising in pipe fabrication.
Our ability to work on-site with our dedicated mobile equipment is essential to our capability to provide a quality maintenance service to our customers. We are capable of providing a full team of qualified boilermakers that can work either to your plan or project manage if a plan has not been developed.
Industry/Entity Type
Industrial
Contact Information for Business Card
company name- CORVAN FAB PTY LTD
story - industrial steel fabrication, constructions and pipelines
Director - Greg Halvey
workshop address - shed 7, 3820 mirren rd Marlow
postal address - P.O BOX 268 MARLOW Q 4871
mobile - 0438596204
w/shop phone - 0740593827
fax - 0740593828
email - admin@corvanfab.com.au
web - www.corvanfab.com.au
Logo Text
CORVAN FAB pty ltd

```html
<!DOCTYPE html>
<html lang="en">
<head>
<meta charset="utf-8">
<title>Corvan Fab Business Card</title>
<link rel="stylesheet" href="https://fonts.googleapis.com/css2?family=Didact+Gothic&family=Arimo:wght@700&display=swap">
<style>
  :root {
    --bg: #e9e8ee;
    --brand: #5f5cab;
    --brand-deep: #4f4c9c;
    --paper: #ffffff;
    --ink: #3f3d86;
    --muted: #8a89b4;
  }
  * { box-sizing: border-box; margin: 0; padding: 0; }
  html, body { width: 1200px; height: 1000px; overflow: hidden; }
  body {
    background: var(--bg);
    font-family: "Didact Gothic", "Century Gothic", sans-serif;
    position: relative;
  }
  .card {
    position: absolute;
    top: 350px;
    width: 525px;
    height: 300px;
    border-radius: 3px;
    box-shadow: 0 6px 20px rgba(40, 38, 80, 0.18);
    overflow: hidden;
  }
  /* contact side */
  .card--back { left: 50px; background: var(--paper); color: var(--ink); }
  .card--back .wordmark {
    position: absolute;
    top: 26px;
    right: 30px;
    font-size: 30px;
    letter-spacing: 1px;
    color: var(--brand);
    line-height: 1;
  }
  .card--back .holder {
    position: absolute;
    left: 30px;
    top: 128px;
  }
  .holder .name { font-size: 25px; color: var(--brand); line-height: 1; }
  .holder .role { font-size: 9px; letter-spacing: 2.5px; color: var(--muted); margin-top: 4px; }
  .card--back .rule {
    position: absolute;
    left: 30px;
    right: 0;
    top: 182px;
    height: 3px;
    background: var(--brand);
  }
  .card--back .contact {
    position: absolute;
    left: 215px;
    top: 104px;
    font-size: 10.5px;
    line-height: 15px;
    color: var(--ink);
    white-space: nowrap;
  }
  .contact b { font-weight: normal; color: var(--brand-deep); }

  /* brand side */
  .card--front {
    left: 625px;
    background: linear-gradient(135deg, #6a67b8 0%, var(--brand) 55%, var(--brand-deep) 100%);
    color: #fff;
    display: flex;
    flex-direction: column;
    align-items: center;
    justify-content: center;
    gap: 18px;
  }
  .card--front .wordmark {
    font-size: 56px;
    letter-spacing: 2px;
    line-height: 1;
    color: #fff;
  }
  .card--front .web {
    font-family: "Arimo", Arial, sans-serif;
    font-weight: 700;
    font-size: 19px;
    letter-spacing: 0.5px;
  }
</style>
</head>
<body>
  <section class="card card--back" aria-label="Business card, contact side">
    <div class="wordmark">CORVAN FAB</div>
    <div class="contact">
      <div>shed 7, 3820 mirren rd Marlow / P.O BOX 268 MARLOW Q 4871</div>
      <div><b>m:</b> 0438596204 &nbsp;<b>w/shop p:</b> 0740593827 &nbsp;<b>f:</b> 0740593828</div>
      <div><b>e:</b> admin@corvanfab.com.au / <b>w:</b> www.corvanfab.com.au</div>
    </div>
    <div class="holder">
      <div class="name">Greg Halvey</div>
      <div class="role">DIRECTOR</div>
    </div>
    <div class="rule"></div>
  </section>

  <section class="card card--front" aria-label="Business card, brand side">
    <div class="wordmark">CORVAN FAB</div>
    <div class="web">www.corvanfab.com.au</div>
  </section>
</body>
</html>
```